Brannigan Ashcroft LLC. custom built/handcrafted

I am recent small business owner looking to sell my art(drawings) and woodworking projects from my home. I have a very rough draft of a simple card design created on a simple digital program. I was hoping for a fancier lettering on the initial letters (BA). More of a calligraphy style. Also, the yellow border around the logo I would like to be a gold foil look. For it to be shiny or reflective look and to keep the other letters black with a consistent font on the card and the card white.

Target Market(s)

Local and neighboring cities

Industry/Entity Type

Art (drawing)/Woodworking

Contact Information for Business Card

My email tpashcroft@mailvane.net, phone number 949-517-3068. In the files provided it has a yellow border around the logo and I was looking to make that a gold foil.

Font styles to use
Serif
Decorative
Script

Requirements
Nice to have
• symbols for having a Pagebook and Lenshare

```html
<!DOCTYPE html>
<html lang="en">
<head>
<meta charset="utf-8">
<title>Brannigan Ashcroft LLC. – Business Card</title>
<link rel="stylesheet" href="https://fonts.googleapis.com/css2?family=Cinzel:wght@700&family=Montserrat:wght@500&display=swap">
<style>
  :root {
    --backdrop: #e9e2d3;
    --card: #ffffff;
    --ink: #1c1412;
    --gold-dark: #b8860b;
    --gold-light: #f3dc8c;
    --shadow: rgba(40, 30, 15, 0.28);
  }
  * { box-sizing: border-box; margin: 0; padding: 0; }
  html, body { width: 1200px; height: 1200px; overflow: hidden; }
  body {
    background: var(--backdrop);
    color: var(--ink);
    font-family: "Cinzel", Georgia, serif;
    position: relative;
  }
  .card {
    position: absolute;
    left: 200px;
    width: 800px;
    height: 457px;
    background: var(--card);
    box-shadow: 0 10px 24px var(--shadow);
  }
  .card--front { top: 120px; }
  .card--back { top: 623px; }

  /* Front side */
  .holder-name {
    position: absolute; top: 70px; left: 0; right: 0;
    text-align: center; font-size: 52px; font-weight: 700; letter-spacing: 1px;
  }
  .holder-role {
    position: absolute; top: 138px; left: 0; right: 0;
    text-align: center; font-size: 40px; font-weight: 700; letter-spacing: 1px;
  }
  .divider {
    position: absolute; top: 222px; left: 56px; right: 56px;
    height: 3px; background: var(--ink);
  }
  .contact {
    position: absolute; top: 250px;
    display: flex; flex-direction: column; align-items: center; gap: 10px;
    font-family: "Montserrat", Arial, sans-serif; font-weight: 500; font-size: 21px;
  }
  .contact--phone { left: 110px; width: 220px; top: 262px; }
  .contact--email { right: 40px; width: 330px; }
  .contact svg { display: block; }
  .socials {
    position: absolute; top: 385px; left: 0; right: 0;
    display: flex; justify-content: center; gap: 44px;
    font-family: "Cinzel", Georgia, serif; font-weight: 700; font-size: 20px;
  }
  .social { display: flex; align-items: center; gap: 8px; }
  .social__dot { width: 22px; height: 22px; background: var(--ink); border-radius: 50%; }
  .social__square { width: 22px; height: 22px; background: var(--ink); border-radius: 4px; }

  /* Back side */
  .gold-frame {
    position: absolute; top: 28px; left: 110px; width: 590px; height: 310px;
    border: 6px solid var(--gold-dark);
    border-image: linear-gradient(100deg, var(--gold-dark) 0%, var(--gold-light) 35%, var(--gold-dark) 60%, var(--gold-light) 80%, var(--gold-dark) 100%) 1;
    display: flex; align-items: center; justify-content: center;
  }
  .brand-name {
    font-size: 44px; font-weight: 700; letter-spacing: 1px; text-align: center; line-height: 1.2;
  }
  .tagline {
    position: absolute; top: 370px; left: 0; right: 0;
    text-align: center; font-size: 38px; font-weight: 700; letter-spacing: 1px;
  }
</style>
</head>
<body>
  <section class="card card--front" aria-label="Card front">
    <h1 class="holder-name">Thomas P. Ashcroft</h1>
    <p class="holder-role">Owner</p>
    <div class="divider"></div>

    <div class="contact contact--phone">
      <svg width="52" height="40" viewBox="0 0 52 40" aria-hidden="true">
        <path d="M4 12 Q26 -2 48 12 L44 18 L36 15 L36 10 Q26 6 16 10 L16 15 L8 18 Z" fill="var(--ink)"/>
        <path d="M14 17 L38 17 L46 36 L6 36 Z" fill="var(--ink)"/>
        <circle cx="26" cy="26" r="6" fill="#fff"/>
        <circle cx="26" cy="26" r="2.5" fill="var(--ink)"/>
      </svg>
      <span>949-517-3068</span>
    </div>

    <div class="contact contact--email">
      <svg width="56" height="40" viewBox="0 0 56 40" aria-hidden="true">
        <rect x="3" y="3" width="50" height="34" fill="none" stroke="var(--ink)" stroke-width="3"/>
        <path d="M3 3 L28 24 L53 3 M3 37 L22 19 M53 37 L34 19" fill="none" stroke="var(--ink)" stroke-width="3"/>
      </svg>
      <span>tpashcroft@mailvane.net</span>
    </div>

    <div class="socials">
      <span class="social"><span class="social__dot"></span>Pagebook</span>
      <span class="social"><span class="social__square"></span>Lenshare</span>
    </div>
  </section>

  <section class="card card--back" aria-label="Card back">
    <div class="gold-frame">
      <p class="brand-name">Brannigan<br>Ashcroft</p>
    </div>
    <p class="tagline">Custom Build • Handcrafted</p>
  </section>
</body>
</html>
```